Brackenfield Prime Healthcare Needs a Business Card Design

We need a business card design for a company based in Shorewood IL called "Brackenfield Prime Healthcare". We provide an integrated medical model involving chiropractic, trigger point injections and other medical services in one location. I have attached our logo to this with the colors being in the puzzle design of the logo. We are looking for a great design that will WOW those around us but also be able to communicate our information easily

Industry/Entity Type

Medical

Contact Information for Business Card

This is a integrated Medical office featuring numerous services to clients in the office.

Requirements
Must have
• Logo

```html
<!DOCTYPE html>
<html lang="en">
<head>
<meta charset="utf-8">
<title>Brackenfield Prime Healthcare – Business Card</title>
<link href="https://fonts.googleapis.com/css2?family=Exo+2:wght@400;500;600&display=swap" rel="stylesheet">
<style>
  :root {
    --backdrop: #e6e6e6;
    --card: #ffffff;
    --brand-blue: #3f7fc0;
    --panel-blue: #7098cb;
    --accent-green: #5fb346;
    --ink: #2b2b2b;
    --ink-soft: #444444;
    --on-panel: #ffffff;
  }
  * { margin: 0; padding: 0; box-sizing: border-box; }
  html, body {
    width: 1200px; height: 900px; overflow: hidden;
    background: var(--backdrop);
    font-family: "Exo 2", Arial, sans-serif;
  }
  .canvas {
    position: relative; width: 1200px; height: 900px;
    display: flex; flex-direction: column; align-items: center; justify-content: center; gap: 44px;
  }
  .card {
    position: relative; width: 660px; height: 377px;
    background: var(--card); overflow: hidden;
    box-shadow: 0 6px 18px rgba(0,0,0,0.12);
  }
  .brand { display: flex; align-items: center; gap: 12px; }
  .brand-square { width: 34px; height: 34px; background: var(--brand-blue); flex: none; }
  .brand-name {
    color: var(--brand-blue); font-weight: 500; font-size: 24px; line-height: 1.05;
    text-transform: uppercase; letter-spacing: 0.5px;
  }
  .card-back .brand { position: absolute; left: 50%; top: 50%; transform: translate(-50%, -50%); }
  .card-front .brand { position: absolute; left: 38px; top: 118px; }
  .card-front .brand-name { font-size: 21px; }
  .card-art { position: absolute; inset: 0; }
  .holder { position: absolute; left: 38px; bottom: 40px; }
  .holder-name {
    font-size: 22px; font-weight: 600; color: var(--ink); letter-spacing: 1.5px; text-transform: uppercase;
  }
  .holder-role { font-size: 16px; color: var(--ink-soft); margin-top: 2px; }
  .contact {
    position: absolute; right: 30px; top: 42px; text-align: right;
    color: var(--on-panel); font-size: 12.5px; line-height: 1.3;
  }
  .contact-address { font-size: 14px; margin-bottom: 16px; }
  .contact-line { display: flex; justify-content: flex-end; align-items: center; gap: 8px; margin-bottom: 9px; }
  .contact-line svg { width: 13px; height: 13px; flex: none; }
</style>
</head>
<body>
<main class="canvas">
  <section class="card card-back" aria-label="Business card back">
    <div class="brand">
      <span class="brand-square"></span>
      <span class="brand-name">Brackenfield Prime<br>Healthcare</span>
    </div>
  </section>

  <section class="card card-front" aria-label="Business card front">
    <svg class="card-art" viewBox="0 0 660 377" width="660" height="377" aria-hidden="true">
      <path d="M385 0 C470 70 440 250 245 377 L660 377 L660 0 Z" fill="var(--accent-green)"/>
      <path d="M405 0 C485 80 450 260 262 377 L660 377 L660 0 Z" fill="var(--panel-blue)"/>
    </svg>

    <div class="brand">
      <span class="brand-square"></span>
      <span class="brand-name">Brackenfield Prime<br>Healthcare</span>
    </div>

    <div class="holder">
      <p class="holder-name">Martin Hollowell</p>
      <p class="holder-role">Managing Director</p>
    </div>

    <div class="contact">
      <p class="contact-address">214 Meadow Street,<br>Plainfield Road</p>
      <p class="contact-line">815 555 0142
        <svg viewBox="0 0 16 16"><path d="M3 1 L6 1 L7 5 L5 6.5 C6 9 7.5 10.5 9.5 11 L11 9 L15 10 L15 13 C15 14 14 15 13 15 C6.5 15 1 9.5 1 3 C1 2 2 1 3 1 Z" fill="currentColor"/></svg>
      </p>
      <p class="contact-line">815 555 0187
        <svg viewBox="0 0 16 16"><rect x="4" y="1" width="8" height="14" rx="1.5" fill="none" stroke="currentColor" stroke-width="1.6"/><circle cx="8" cy="12.3" r="0.9" fill="currentColor"/></svg>
      </p>
      <p class="contact-line">815 555 0163
        <svg viewBox="0 0 16 16"><rect x="1" y="6" width="14" height="8" rx="1" fill="currentColor"/><rect x="4" y="2" width="8" height="5" fill="currentColor"/></svg>
      </p>
      <p class="contact-line">info@brackenfield.com
        <svg viewBox="0 0 16 16"><rect x="1" y="3" width="14" height="10" rx="1" fill="currentColor"/><path d="M1.5 3.5 L8 9 L14.5 3.5" fill="none" stroke="var(--panel-blue)" stroke-width="1.4"/></svg>
      </p>
      <p class="contact-line">www.brackenfield.com
        <svg viewBox="0 0 16 16"><circle cx="8" cy="8" r="6.5" fill="none" stroke="currentColor" stroke-width="1.4"/><ellipse cx="8" cy="8" rx="3" ry="6.5" fill="none" stroke="currentColor" stroke-width="1.1"/><path d="M1.5 8 H14.5" stroke="currentColor" stroke-width="1.1"/></svg>
      </p>
    </div>
  </section>
</main>
</body>
</html>
```